Updated Business Card Re-design (Logo Provided)

I am needing to update our business cards for our practice, Bright Harbor Care. We are a personal injury and wellness practice. The final design should be elegant and classy, but a type of card people would want to keep. Any samples should only have Dr. Tarek Minouvel on the template.
Updates

Went on vacation/holiday

Need extra days to review

Target Market(s)

Personal Injury clients, wellness clients

Industry/Entity Type

Personal Injury, medical, wellness

Contact Information for Business Card

dr and practice name, offerings

Requirements
Must have
• Single sided, this will be printed on a transparent business card, no exceptions.

```html
<!DOCTYPE html>
<html lang="en">
<head>
<meta charset="utf-8">
<title>Bright Harbor Care — Business Card</title>
<link rel="stylesheet" href="https://fonts.googleapis.com/css2?family=Montserrat:wght@800&family=Oswald:wght@600&family=Poppins:wght@400&display=swap">
<style>
  :root {
    --page: #e8e5e4;
    --card: #f6f3f2;
    --blue: #1175bf;
    --orange: #f39321;
    --green: #2e8b45;
    --ink: #2a2a2a;
  }
  html, body {
    margin: 0;
    width: 1200px;
    height: 900px;
    overflow: hidden;
    background: var(--page);
  }
  .business-card {
    position: absolute;
    left: 55px;
    top: 113px;
    width: 1090px;
    height: 673px;
    background: var(--card);
    box-shadow: 0 10px 30px rgba(0,0,0,0.12);
    overflow: hidden;
  }
  .card-waves {
    position: absolute;
    inset: 0;
    width: 100%;
    height: 100%;
  }
  .brand {
    position: absolute;
    left: 40px;
    width: 480px;
    top: 175px;
    text-align: center;
    font-family: "Montserrat", sans-serif;
    font-weight: 800;
    color: var(--blue);
    letter-spacing: -1.5px;
  }
  .brand-dot {
    display: block;
    width: 56px;
    height: 56px;
    margin: 0 auto 40px;
    border-radius: 50%;
    background: var(--orange);
  }
  .brand-name {
    margin: 0;
    font-size: 46px;
    line-height: 1.05;
  }
  .brand-name .brand-line-small {
    display: block;
    font-size: 34px;
    letter-spacing: 0;
  }
  .divider {
    position: absolute;
    left: 544px;
    top: 160px;
    width: 2px;
    height: 315px;
    background: var(--green);
  }
  .doctor-name {
    position: absolute;
    left: 582px;
    top: 140px;
    margin: 0;
    font-family: "Oswald", sans-serif;
    font-weight: 600;
    font-size: 44px;
    color: var(--blue);
    letter-spacing: -0.5px;
    line-height: 60px;
  }
  .services {
    position: absolute;
    left: 578px;
    top: 225px;
    margin: 0;
    padding: 0;
    list-style: none;
    font-family: "Poppins", sans-serif;
    font-size: 29px;
    color: var(--ink);
  }
  .services li {
    display: flex;
    align-items: center;
    height: 53px;
  }
  .services li::before {
    content: "";
    width: 14px;
    height: 14px;
    margin: 0 16px 0 6px;
    border-radius: 50%;
    background: var(--orange);
    box-shadow: 6px 0 0 var(--blue);
  }
</style>
</head>
<body>
  <main class="business-card">
    <svg class="card-waves" viewBox="0 0 1090 673" aria-hidden="true">
      <path d="M540 610 C790 555 960 475 1090 392 L1090 673 L540 673 Z" fill="var(--green)"/>
      <path d="M0 618 C300 608 700 548 1090 438 L1090 673 L0 673 Z" fill="var(--orange)"/>
      <path d="M0 630 C320 620 720 565 1090 482 L1090 673 L0 673 Z" fill="var(--blue)"/>
      <path d="M0 654 C340 648 740 600 1090 512" fill="none" stroke="var(--orange)" stroke-width="9"/>
    </svg>

    <div class="brand">
      <span class="brand-dot"></span>
      <h2 class="brand-name">BRIGHT HARBOR<span class="brand-line-small">CARE</span></h2>
    </div>

    <div class="divider"></div>

    <h1 class="doctor-name">DR. TAREK MINOUVEL, D.C.</h1>
    <ul class="services">
      <li>Auto Accident Care</li>
      <li>Primary Care</li>
      <li>Medical Weight loss</li>
      <li>Physical Therapy</li>
      <li>Chiropractic</li>
    </ul>
  </main>
</body>
</html>
```